Business Card

We need some ideas for corporate business cards. I'm interested in a double sided card, with one side featuring our corporate logo, the other side with employee information.

Corporate colors, logo etc. available at www.brivalo.com

Industry/Entity Type

Business

Requirements
Must have
• The "Brivalo" logo with stylized "O"

Nice to have
• Preferred font is calibri

```html
<!DOCTYPE html>
<html lang="en">
<head>
<meta charset="utf-8">
<title>Brivalo Business Card</title>
<link rel="stylesheet" href="https://fonts.googleapis.com/css2?family=Open+Sans:wght@400;600;700&display=swap">
<style>
  :root {
    --page: #d9d9d9;
    --paper: #f2f2f0;
    --brand-blue: #3e5285;
    --band-grey: #9b9b9b;
    --ink: #2a2a2a;
    --ink-soft: #555555;
    --light-text: #eeeeee;
    --icon-orange: #e89a2c;
    --icon-teal: #2b8b9b;
    --icon-red: #b83b4d;
  }
  * { box-sizing: border-box; margin: 0; padding: 0; }
  html, body { width: 1200px; height: 1000px; overflow: hidden; }
  body {
    background: var(--page);
    font-family: "Open Sans", Calibri, sans-serif;
    position: relative;
  }
  .card {
    position: absolute;
    left: 200px;
    width: 800px;
    height: 460px;
    background: var(--paper);
    overflow: hidden;
    box-shadow: 0 4px 14px rgba(0,0,0,0.18);
  }
  .card--contact { top: 30px; }
  .card--brand { top: 510px; }
  .card__bands { position: absolute; inset: 0; }

  .wordmark {
    position: absolute;
    top: 34px; left: 40px;
    display: flex; align-items: center; gap: 10px;
    color: var(--brand-blue);
    font-weight: 700; font-size: 22px; letter-spacing: 4px;
  }
  .wordmark__square { width: 18px; height: 18px; background: var(--brand-blue); }

  .contact-list {
    position: absolute; top: 138px; left: 40px;
    list-style: none;
    color: var(--light-text);
    font-size: 13px; line-height: 17px;
  }
  .contact-list li { display: flex; align-items: flex-start; gap: 10px; margin-bottom: 6px; }
  .contact-list svg { flex: none; width: 22px; height: 22px; }

  .brand-name {
    position: absolute;
    color: var(--paper);
    font-weight: 700;
    letter-spacing: 2px;
  }
  .card--contact .brand-name { right: 60px; top: 250px; font-size: 64px; }
  .card--brand .brand-name { left: 60px; top: 60px; font-size: 64px; }

  .intro {
    position: absolute; right: 30px; top: 246px; width: 420px;
    color: var(--light-text);
    font-size: 10.5px; line-height: 14px; text-align: center;
  }

  .pillars {
    position: absolute; left: 0; right: 0; top: 318px;
    display: flex; justify-content: space-around; padding: 0 30px;
  }
  .pillar { width: 210px; text-align: center; }
  .pillar svg { width: 34px; height: 34px; }
  .pillar__title { font-weight: 700; font-size: 17px; color: var(--ink); margin: 4px 0 4px; }
  .pillar__text { font-size: 10.5px; line-height: 13px; color: var(--ink-soft); }
</style>
</head>
<body>

<section class="card card--contact" aria-label="Card front with contact details">
  <svg class="card__bands" viewBox="0 0 800 460" preserveAspectRatio="none" aria-hidden="true">
    <rect x="0" y="118" width="800" height="342" fill="var(--band-grey)"/>
    <polygon points="0,300 800,100 800,350 0,460" fill="var(--brand-blue)"/>
    <rect x="0" y="0" width="800" height="118" fill="var(--paper)"/>
  </svg>

  <div class="wordmark"><span class="wordmark__square"></span>BRIVALO</div>

  <ul class="contact-list">
    <li>
      <svg viewBox="0 0 22 22"><circle cx="11" cy="11" r="11" fill="var(--icon-orange)"/><path d="M7 6h3l1 3-2 1a7 7 0 0 0 3 3l1-2 3 1v3c-6 0-9-3-9-9z" fill="#fff"/></svg>
      <span>+000 - 2468 - 1357<br>+000 - 3141 - 5926</span>
    </li>
    <li>
      <svg viewBox="0 0 22 22"><circle cx="11" cy="11" r="11" fill="var(--icon-teal)"/><circle cx="11" cy="11" r="6" fill="none" stroke="#fff" stroke-width="1.4"/><ellipse cx="11" cy="11" rx="2.6" ry="6" fill="none" stroke="#fff" stroke-width="1.2"/><line x1="5" y1="11" x2="17" y2="11" stroke="#fff" stroke-width="1.2"/></svg>
      <span>admin@brivalo.com<br>www.brivalo.com</span>
    </li>
    <li>
      <svg viewBox="0 0 22 22"><circle cx="11" cy="11" r="11" fill="var(--icon-red)"/><path d="M5 11l6-5 6 5h-2v5h-3v-3h-2v3H7v-5z" fill="#fff"/></svg>
      <span>48 Harrow Lane,<br>Leeds LS2 7QD</span>
    </li>
  </ul>

  <div class="brand-name">Brivalo</div>
</section>

<section class="card card--brand" aria-label="Card back with company overview">
  <svg class="card__bands" viewBox="0 0 800 460" preserveAspectRatio="none" aria-hidden="true">
    <rect x="0" y="150" width="800" height="152" fill="var(--band-grey)"/>
    <polygon points="0,0 800,0 800,150 0,302" fill="var(--brand-blue)"/>
  </svg>

  <div class="brand-name">Brivalo</div>

  <p class="intro">Brivalo software is the foundation for a variety of solutions used by the world's largest operators to innovate business models related to how people, machines and services interact with their network.</p>

  <div class="pillars">
    <div class="pillar">
      <svg viewBox="0 0 34 34" aria-hidden="true">
        <g fill="var(--brand-blue)">
          <circle cx="17" cy="17" r="10"/>
          <rect x="14.5" y="3" width="5" height="6"/><rect x="14.5" y="25" width="5" height="6"/>
          <rect x="3" y="14.5" width="6" height="5"/><rect x="25" y="14.5" width="6" height="5"/>
          <rect x="14.5" y="3" width="5" height="6" transform="rotate(45 17 17)"/>
          <rect x="14.5" y="25" width="5" height="6" transform="rotate(45 17 17)"/>
          <rect x="3" y="14.5" width="6" height="5" transform="rotate(45 17 17)"/>
          <rect x="25" y="14.5" width="6" height="5" transform="rotate(45 17 17)"/>
        </g>
        <circle cx="17" cy="17" r="4.5" fill="var(--paper)"/>
      </svg>
      <h3 class="pillar__title">Technology</h3>
      <p class="pillar__text">Software that controls the data quality, network services, and pricing options available to any connected device.</p>
    </div>
    <div class="pillar">
      <svg viewBox="0 0 34 34" aria-hidden="true">
        <circle cx="17" cy="17" r="14" fill="var(--brand-blue)"/>
        <circle cx="17" cy="17" r="10" fill="none" stroke="var(--paper)" stroke-width="1.6"/>
        <polygon points="22,12 18.5,18.5 12,22 15.5,15.5" fill="var(--paper)"/>
      </svg>
      <h3 class="pillar__title">Solutions</h3>
      <p class="pillar__text">The world's largest Service Providers use our solutions to commercialize and analyze the activity on their networks.</p>
    </div>
    <div class="pillar">
      <svg viewBox="0 0 34 34" aria-hidden="true">
        <path d="M2 17C8 8 26 8 32 17C26 26 8 26 2 17z" fill="var(--brand-blue)"/>
        <circle cx="17" cy="17" r="6" fill="var(--paper)"/>
        <circle cx="17" cy="17" r="3.5" fill="var(--brand-blue)"/>
      </svg>
      <h3 class="pillar__title">Vision</h3>
      <p class="pillar__text">A comprehensive platform that enables Service Providers to meet the diverse needs of an increasingly connected world.</p>
    </div>
  </div>
</section>

</body>
</html>
```